New, High-Tech Website for Venture Z - A Product Development Company

Venture Z is located in Silicon Valley, CA. We help companies build products from start to finish and everywhere in between. We build teams with top talent based on our customer's needs. We need a BRAND NEW website that looks innovative, fresh, new & modern. We want our website to impress companies that will hire us, as well as developers, designers, product people, etc.

The design is very important!

Target Market(s)

Small companies, entrepreneurs, anyone who needs help building a product or finding top talent

Industry/Entity Type

Tech

Coding

Coded - Design and coding required

Font styles to use
Sans Serif

Requirements
Must have
• Our logo (attached) and colors that look good with the logo.

**UPDATE - Site should be fully coded for WordPress and be MOBILE FRIENDLY. (Responsive Designs)
Nice to have
• We would love to see your ideas and if you have any other cool ideas to make our site POP and look attractive.

Please also let us know the following when you submit your design (in the notes section)!

1) Are we able to use any illustrations or images you provided legally? Would we need to pay any additional fees for images or illustrations?  If so, how much per picture/illustration?

2) If we choose your design, do your services include deploying the design to our Wordpress site?  Or, do you charge extra for this and how much?

3) If we choose your design, will this include any other page designs?  If so, how many?

4) If we choose your design, how much will you charge to design and implement other pages for us (like our contact us page, careers page, site map page, etc.) so our website looks cohesive?

5) What is your turnaround time for further page designs and implementations to the site?

6) Can you design AND implement surveys and/or custom questionnaires? What is the cost?
Should not have
• Nothing too "corporate" looking. For example, no images with men in suits around a large conference room because this doesn't represent who we are. We are more looking for images of people working - small startup company style.

Really cool, high tech illustrations are good too.

```html
<!DOCTYPE html>
<html lang="en">
<head>
<meta charset="utf-8">
<title>Venture Z — Product Development</title>
<link rel="stylesheet" href="https://fonts.googleapis.com/css2?family=Lato:wght@400;700;900&display=swap">
<style>
:root{
  --teal:#2bb3a3;
  --sky:#29b6e8;
  --grad:linear-gradient(90deg,#29b8ec,#2db3a0);
  --ink:#3a3a3a;
  --text:#444;
  --muted:#f1f1f1;
  --foot:#2b2b2b;
  --white:#fff;
}
*{box-sizing:border-box;margin:0;padding:0}
html,body{width:1200px;height:4271px;overflow:hidden}
body{font-family:'Lato',sans-serif;color:var(--text);background:var(--white);position:relative}
.btn{position:absolute;display:flex;align-items:center;justify-content:center;background:var(--grad);color:var(--white);font-weight:700;text-transform:uppercase;text-decoration:none}
.btn-read{width:186px;height:52px;font-size:19px;letter-spacing:.3px}
h2.section-title{position:absolute;font-size:34px;font-weight:900;color:var(--ink);text-transform:uppercase;letter-spacing:.2px}

/* hero */
.hero{position:absolute;left:0;top:0;width:1200px;height:802px;background:linear-gradient(180deg,#6f8aa3 0%,#8c8a7f 22%,#4f5447 45%,#3a3f35 70%,#2f3430 100%)}
.brand{position:absolute;left:75px;top:96px;color:var(--white);font-size:22px;font-weight:700;display:flex;align-items:center;gap:10px}
.brand .dot{width:26px;height:26px;border-radius:50%;background:var(--grad)}
.top-btn{height:40px;font-size:14px;top:51px;width:257px}
.nav{position:absolute;top:119px;left:0;width:1200px;height:24px}
.nav a{position:absolute;color:var(--white);font-size:17px;text-decoration:none;text-transform:uppercase;letter-spacing:.3px}
.hero-title{position:absolute;top:400px;width:1200px;text-align:center;color:var(--white);font-size:60px;font-weight:900;letter-spacing:.5px}
.hero-sub{position:absolute;top:478px;width:1200px;text-align:center;color:var(--white);font-size:28px;line-height:42px}

/* about */
.about-disc{position:absolute;left:75px;top:873px;width:436px;height:436px;border-radius:50%;background:linear-gradient(45deg,#2db3a0,#29b8ec);opacity:.9}
.about-copy{position:absolute;left:617px;top:1003px;width:515px;font-size:17px;line-height:31.5px;color:var(--text)}

/* we love */
.love{position:absolute;left:0;top:1389px;width:1200px;height:522px;background:linear-gradient(135deg,#1a5f6b,#2a8e8f 45%,#1d6c74)}
.love-title{position:absolute;top:1452px;width:1200px;text-align:center;color:var(--white);font-size:34px;font-weight:900}
.card{position:absolute;top:1530px;width:330px;height:244px;background:var(--white);text-align:center;font-size:17.5px;line-height:30px;color:var(--text)}
.card svg{position:absolute;left:50%;transform:translateX(-50%)}
.card p{position:absolute;left:26px;right:26px}
.dots span{position:absolute;top:1826px;width:13px;height:13px}

/* feature rows */
.photo-circle{position:absolute;border-radius:50%;border:5px solid var(--teal)}
.badge{position:absolute;width:110px;height:110px;border-radius:50%;background:var(--teal);border:6px solid var(--white);display:flex;align-items:center;justify-content:center}
.checklist{position:absolute;list-style:none;font-size:17px;color:var(--text)}
.checklist li{height:38px;display:flex;align-items:center;gap:16px}

/* services */
.services{position:absolute;left:0;top:2997px;width:1200px;height:865px;background:var(--muted)}
.services-sub{position:absolute;top:3106px;width:1200px;text-align:center;font-size:17px;color:var(--text)}
.tile{position:absolute;width:512px;height:287px;overflow:hidden}
.tile-label{position:absolute;left:0;bottom:0;width:330px;height:64px;background:var(--teal);opacity:.92;clip-path:polygon(0 0,88% 0,100% 100%,0 100%);color:var(--white);font-size:23px;font-weight:900;padding:18px 0 0 23px;text-transform:uppercase}

/* footer */
.footer{position:absolute;left:0;top:3862px;width:1200px;height:409px;background:var(--foot);color:var(--white)}
.foot-col{position:absolute;top:3925px}
.foot-col h4{color:var(--teal);font-size:17px;font-weight:700;text-transform:uppercase;margin-bottom:12px}
.foot-col a{display:block;color:var(--white);font-size:14px;text-decoration:none;height:36px}
.copyright{position:absolute;left:75px;top:4217px;font-size:13px;color:var(--white)}
.social span{position:absolute;top:4218px;width:18px;height:18px;border-radius:50%;border:2px solid var(--white)}
</style>
</head>
<body>

<header class="hero" role="img" aria-label="Aerial photo of Silicon Valley with freeways and mountains at dusk"></header>
<div class="brand"><span class="dot"></span>Venture Z</div>
<a class="btn top-btn" style="left:602px">Freelancers - Apply Now</a>
<a class="btn top-btn" style="left:870px">Companies - Get In Touch</a>
<nav class="nav">
  <a style="left:494px">Services</a>
  <a style="left:615px">About</a>
  <a style="left:719px">Testimonials &amp; Press</a>
  <a style="left:961px">Careers</a>
  <a style="left:1081px">Blog</a>
</nav>
<h1 class="hero-title">WELCOME TO VENTURE Z</h1>
<p class="hero-sub">Product-led, team-driven software development<br>based in Silicon Valley, CA</p>

<!-- about -->
<div class="about-disc" aria-hidden="true"></div>
<h2 class="section-title" style="left:617px;top:898px">About Venture Z</h2>
<p class="about-copy">We take a product-led, team-driven approach to software development, establishing the product mindset in early stage companies, and transforming to a product mindset in more mature companies.&nbsp; We are obsessed with building teams with the best people and then removing any obstacles preventing them from doing their best work.&nbsp; Team is at the heart of what we do and how we deliver great products.</p>
<a class="btn btn-read" style="left:617px;top:1218px">Read More</a>

<!-- we love -->
<section class="love" role="img" aria-label="Teal toned photo of gears and a glowing light bulb"></section>
<h2 class="love-title">WE LOVE TO WORK WITH</h2>
<div class="card" style="left:75px">
  <svg style="top:34px" width="44" height="64" viewBox="0 0 44 64"><path d="M22 2a20 20 0 0 0-12 36c3 3 4 6 4 10h16c0-4 1-7 4-10A20 20 0 0 0 22 2z" fill="var(--sky)"/><rect x="14" y="52" width="16" height="5" rx="2" fill="var(--teal)"/><rect x="16" y="59" width="12" height="4" rx="2" fill="var(--teal)"/></svg>
  <p style="top:120px">Entrepreneurs with an idea who want to build a prototype</p>
</div>
<div class="card" style="left:436px">
  <svg style="top:34px" width="64" height="64" viewBox="0 0 64 64"><path d="M60 4C44 4 32 12 24 26l14 14C52 32 60 20 60 4z" fill="var(--sky)"/><path d="M22 28l-12 2-6 10 14-2zM36 42l-2 12-10 6 2-14z" fill="var(--teal)"/><path d="M18 44l-10 12 12-10z" fill="var(--teal)"/><circle cx="44" cy="20" r="5" fill="#fff"/></svg>
  <p style="top:120px">Start Up Companies who need a product built quickly and cost&nbsp; effectively</p>
</div>
<div class="card" style="left:797px">
  <svg style="top:40px" width="88" height="52" viewBox="0 0 88 52"><circle cx="44" cy="12" r="11" fill="var(--sky)"/><path d="M24 52c0-14 9-22 20-22s20 8 20 22z" fill="var(--sky)"/><circle cx="16" cy="18" r="8" fill="var(--teal)"/><path d="M0 50c0-10 7-16 16-16 4 0 7 1 9 3-3 4-5 8-5 13z" fill="var(--teal)"/><circle cx="72" cy="18" r="8" fill="var(--teal)"/><path d="M88 50c0-10-7-16-16-16-4 0-7 1-9 3 3 4 5 8 5 13z" fill="var(--teal)"/></svg>
  <p style="top:102px">Small or medium-sized, more established companies that want to ship great products faster, or simply ship</p>
</div>
<div class="dots"><span style="left:581px;background:#222"></span><span style="left:607px;background:#fff"></span></div>

<!-- things that excite us -->
<div class="photo-circle" role="img" aria-label="Photo of a hand drawing a cloud network diagram on a digital screen" style="left:99px;top:1982px;width:478px;height:478px;background:radial-gradient(circle at 40% 40%,#4f8ed8,#1f4f9a 70%,#163a72)"></div>
<div class="badge" style="left:479px;top:1987px">
  <svg width="54" height="50" viewBox="0 0 54 50" fill="#fff"><circle cx="20" cy="30" r="14"/><circle cx="20" cy="30" r="5" fill="var(--teal)"/><circle cx="42" cy="12" r="9"/><circle cx="42" cy="12" r="3" fill="var(--teal)"/><circle cx="44" cy="38" r="7"/><circle cx="44" cy="38" r="2.5" fill="var(--teal)"/></svg>
</div>
<h2 class="section-title" style="left:643px;top:1976px">Things That Excite Us</h2>
<ul class="checklist" style="left:643px;top:2033px">
  <li><svg width="16" height="16" viewBox="0 0 16 16"><circle cx="8" cy="8" r="7" fill="none" stroke="var(--teal)" stroke-width="1.5"/><path d="M4.5 8l2.5 2.5 4.5-5" fill="none" stroke="var(--teal)" stroke-width="1.5"/></svg>Innovation</li>
  <li><svg width="16" height="16" viewBox="0 0 16 16"><circle cx="8" cy="8" r="7" fill="none" stroke="var(--teal)" stroke-width="1.5"/><path d="M4.5 8l2.5 2.5 4.5-5" fill="none" stroke="var(--teal)" stroke-width="1.5"/></svg>New design &amp; technology</li>
  <li><svg width="16" height="16" viewBox="0 0 16 16"><circle cx="8" cy="8" r="7" fill="none" stroke="var(--teal)" stroke-width="1.5"/><path d="M4.5 8l2.5 2.5 4.5-5" fill="none" stroke="var(--teal)" stroke-width="1.5"/></svg>Clear Roadmaps</li>
  <li><svg width="16" height="16" viewBox="0 0 16 16"><circle cx="8" cy="8" r="7" fill="none" stroke="var(--teal)" stroke-width="1.5"/><path d="M4.5 8l2.5 2.5 4.5-5" fill="none" stroke="var(--teal)" stroke-width="1.5"/></svg>Product Releases</li>
  <li><svg width="16" height="16" viewBox="0 0 16 16"><circle cx="8" cy="8" r="7" fill="none" stroke="var(--teal)" stroke-width="1.5"/><path d="M4.5 8l2.5 2.5 4.5-5" fill="none" stroke="var(--teal)" stroke-width="1.5"/></svg>Brining ideas to life</li>
  <li><svg width="16" height="16" viewBox="0 0 16 16"><circle cx="8" cy="8" r="7" fill="none" stroke="var(--teal)" stroke-width="1.5"/><path d="M4.5 8l2.5 2.5 4.5-5" fill="none" stroke="var(--teal)" stroke-width="1.5"/></svg>Solving Busines Challenges</li>
  <li><svg width="16" height="16" viewBox="0 0 16 16"><circle cx="8" cy="8" r="7" fill="none" stroke="var(--teal)" stroke-width="1.5"/><path d="M4.5 8l2.5 2.5 4.5-5" fill="none" stroke="var(--teal)" stroke-width="1.5"/></svg>Happy Clients</li>
</ul>
<a class="btn btn-read" style="left:643px;top:2332px">Read More</a>

<!-- things that we promise -->
<h2 class="section-title" style="left:75px;top:2530px">Things That We Promise</h2>
<ul class="checklist" style="left:75px;top:2585px">
  <li><svg width="16" height="16" viewBox="0 0 16 16"><circle cx="8" cy="8" r="7" fill="none" stroke="var(--teal)" stroke-width="1.5"/><path d="M4.5 8l2.5 2.5 4.5-5" fill="none" stroke="var(--teal)" stroke-width="1.5"/></svg>Experience, Passion &amp; Impact</li>
  <li><svg width="16" height="16" viewBox="0 0 16 16"><circle cx="8" cy="8" r="7" fill="none" stroke="var(--teal)" stroke-width="1.5"/><path d="M4.5 8l2.5 2.5 4.5-5" fill="none" stroke="var(--teal)" stroke-width="1.5"/></svg>Focused strategies</li>
  <li><svg width="16" height="16" viewBox="0 0 16 16"><circle cx="8" cy="8" r="7" fill="none" stroke="var(--teal)" stroke-width="1.5"/><path d="M4.5 8l2.5 2.5 4.5-5" fill="none" stroke="var(--teal)" stroke-width="1.5"/></svg>Great People &amp; High Functioning Teams</li>
  <li><svg width="16" height="16" viewBox="0 0 16 16"><circle cx="8" cy="8" r="7" fill="none" stroke="var(--teal)" stroke-width="1.5"/><path d="M4.5 8l2.5 2.5 4.5-5" fill="none" stroke="var(--teal)" stroke-width="1.5"/></svg>Integrity, Reliability &amp; Security</li>
  <li><svg width="16" height="16" viewBox="0 0 16 16"><circle cx="8" cy="8" r="7" fill="none" stroke="var(--teal)" stroke-width="1.5"/><path d="M4.5 8l2.5 2.5 4.5-5" fill="none" stroke="var(--teal)" stroke-width="1.5"/></svg>Data driven &amp; Design centric results</li>
  <li><svg width="16" height="16" viewBox="0 0 16 16"><circle cx="8" cy="8" r="7" fill="none" stroke="var(--teal)" stroke-width="1.5"/><path d="M4.5 8l2.5 2.5 4.5-5" fill="none" stroke="var(--teal)" stroke-width="1.5"/></svg>Top customer service for our clients</li>
</ul>
<a class="btn btn-read" style="left:76px;top:2844px">Read More</a>
<div class="photo-circle" role="img" aria-label="Photo of a lens held up to view a bright office corridor" style="left:630px;top:2453px;width:480px;height:480px;background:linear-gradient(160deg,#4a7fc0 0%,#3f6fae 45%,#8a5a3c 80%,#a24a22 100%)"></div>
<div class="badge" style="left:612px;top:2518px">
  <svg width="50" height="48" viewBox="0 0 50 48" fill="#fff"><rect x="2" y="20" width="11" height="26" rx="2"/><path d="M17 20l10-18c5 0 7 4 6 9l-2 7h13c3 0 5 3 4 6l-5 18c-1 3-3 4-6 4H17z"/></svg>
</div>

<!-- services -->
<section class="services"></section>
<h2 class="section-title" style="left:0;width:1200px;text-align:center;top:3053px">Our Services</h2>
<p class="services-sub">We build teams that deliver!</p>
<div class="tile" role="img" aria-label="Photo of engineers researching around lab equipment" style="left:75px;top:3172px;background:linear-gradient(120deg,#2c3a4a,#4d6781 55%,#1f2a36)"><div class="tile-label">Research</div></div>
<div class="tile" role="img" aria-label="Photo of a team reviewing design plans on a table" style="left:615px;top:3172px;background:linear-gradient(120deg,#c7ccd2,#8a9bb0 50%,#5b7190)"><div class="tile-label">Design</div></div>
<div class="tile" role="img" aria-label="Photo of engineers in hard hats using a tablet in a factory" style="left:75px;top:3490px;background:linear-gradient(120deg,#5c5f63,#9aa1a8 50%,#d9dcdf)"><div class="tile-label">Engineers</div></div>
<div class="tile" role="img" aria-label="Photo of product managers discussing work at a computer screen" style="left:615px;top:3490px;background:linear-gradient(120deg,#d7dde4,#7e93ad 45%,#1e3b66)"><div class="tile-label">Product Managers</div></div>

<!-- footer -->
<footer class="footer"></footer>
<div class="brand" style="top:4040px;font-size:22px"><span class="dot"></span>Venture Z</div>
<div class="foot-col" style="left:343px">
  <h4>Company</h4>
  <a>Services</a><a>About</a><a>Testimonials &amp; Press</a><a>Careers</a><a>Blog</a>
</div>
<div class="foot-col" style="left:617px">
  <h4>Quick Links</h4>
  <a>Services</a><a>Our Approach</a><a>Why Us</a><a>FAQ</a>
</div>
<div class="foot-col" style="left:883px">
  <h4>Other Links</h4>
  <a>Privacy Policy</a><a>Terms &amp; Conditions</a><a>Security &amp; Compliance</a><a>Subscribe to our blog</a>
</div>
<p class="copyright">Copyright © 2021. Company Name.&nbsp; All Right Reserved</p>
<div class="social"><span style="left:1040px"></span><span style="left:1073px"></span><span style="left:1106px"></span></div>

</body>
</html>
```